Hall of Fame annnouncement graphic for social media

I need a social media Hall of Fame announcement designed in the styles of some of the examples I've posted. I have attached the two gentlemens head shots ... the names are Dale Prusky and Ted Marrish

It is for the BRANDMOOR LINKS HALL OF FAME also include 2026 Inductees ... I have also attached the logo... make the post in similar colors as the logo.

I need this tomorrow so I am going to pick a winner in the next 24 hours.

```html
<!DOCTYPE html>
<html lang="en">
<head>
<meta charset="utf-8">
<title>Brandmoor Links Hall of Fame – 2026 Inductees</title>
<link href="https://fonts.googleapis.com/css2?family=Anton&family=Yellowtail&display=swap" rel="stylesheet">
<style>
  :root {
    --stage: #a9a9a9;
    --navy: #002d79;
    --red: #b01a10;
    --yellow: #fdd200;
    --ink: #222222;
    --paper: #ffffff;
    --mist-top: #f1f1f2;
    --mist-bottom: #dcdde0;
  }
  html, body {
    margin: 0;
    width: 1200px;
    height: 1111px;
    overflow: hidden;
    background: var(--stage);
  }
  .announcement {
    position: absolute;
    left: 62px;
    top: 253px;
    width: 1075px;
    height: 605px;
    display: block;
  }
  .display { font-family: "Anton", "Oswald", sans-serif; }
  .script { font-family: "Yellowtail", cursive; }
  .band-navy { fill: var(--navy); }
  .band-red { fill: var(--red); }
  .hairline { stroke: var(--paper); stroke-width: 1.5; }
  .headline-kicker { fill: var(--red); font-size: 62px; }
  .headline-main { fill: var(--navy); }
  .brand-name { fill: var(--navy); font-size: 21px; letter-spacing: 1px; }
  .inductees-title { fill: var(--red); font-size: 60px; }
  .frame { fill: var(--paper); }
  .pin { fill: var(--red); }
  .pin-head { fill: #d3343a; }
  .name-tag { fill: var(--yellow); }
  .name-dot { fill: var(--ink); }
  .name-text { fill: var(--ink); font-size: 31px; }
</style>
</head>
<body>
<svg class="announcement" viewBox="0 0 1075 605" xmlns="http://www.w3.org/2000/svg">
  <defs>
    <linearGradient id="course-mist" x1="0" y1="0" x2="0" y2="1">
      <stop offset="0" stop-color="var(--mist-top)"/>
      <stop offset="1" stop-color="var(--mist-bottom)"/>
    </linearGradient>
    <linearGradient id="portrait-warm" x1="0" y1="0" x2="0" y2="1">
      <stop offset="0" stop-color="#e9e3df"/>
      <stop offset="0.55" stop-color="#d9a48a"/>
      <stop offset="1" stop-color="#eeeeee"/>
    </linearGradient>
    <linearGradient id="portrait-sky" x1="0" y1="0" x2="0" y2="1">
      <stop offset="0" stop-color="#d8d2e6"/>
      <stop offset="0.55" stop-color="#d7a895"/>
      <stop offset="1" stop-color="#f1e2e8"/>
    </linearGradient>
  </defs>

  <rect class="course-backdrop" x="0" y="0" width="1075" height="605" fill="url(#course-mist)" role="img" aria-label="Faded photo of a golf course green with clubhouse, trees and a gallery of spectators"/>

  <polygon class="band-red" points="0,0 640,0 0,128"/>
  <polygon class="band-navy" points="0,0 484,0 0,120"/>
  <line class="hairline" x1="0" y1="98" x2="163" y2="62"/>

  <polygon class="band-red" points="445,605 1075,480 1075,605"/>
  <polygon class="band-navy" points="605,605 1075,492 1075,605"/>
  <line class="hairline" x1="1031" y1="517" x2="1075" y2="508"/>

  <text class="display brand-name" x="265" y="138" text-anchor="middle">BRANDMOOR LINKS</text>
  <text class="display brand-name" x="265" y="164" text-anchor="middle">HALL OF FAME</text>

  <text class="display headline-kicker" x="71" y="249" textLength="395" lengthAdjust="spacingAndGlyphs">BRANDMOOR LINKS</text>
  <text class="display headline-main" x="71" y="372" font-size="140" textLength="396" lengthAdjust="spacingAndGlyphs">HALL OF</text>
  <text class="display headline-main" x="71" y="553" font-size="205" textLength="398" lengthAdjust="spacingAndGlyphs">FAME</text>

  <text class="script inductees-title" x="771" y="112" text-anchor="middle">2026 Inductees</text>

  <g class="inductee-photo" transform="rotate(4 631 316)">
    <rect class="frame" x="506" y="148" width="250" height="338"/>
    <rect x="518" y="160" width="226" height="320" fill="url(#portrait-warm)" role="img" aria-label="Head shot of inductee Dale Prusky in a white polo shirt"/>
  </g>
  <g class="inductee-photo" transform="rotate(-4 892 310)">
    <rect class="frame" x="768" y="143" width="252" height="338"/>
    <rect x="780" y="155" width="228" height="320" fill="url(#portrait-sky)" role="img" aria-label="Head shot of inductee Ted Marrish in a light pink polo shirt"/>
  </g>

  <circle class="pin" cx="648" cy="166" r="20"/>
  <circle class="pin-head" cx="640" cy="157" r="12"/>
  <circle class="pin" cx="882" cy="166" r="20"/>
  <circle class="pin-head" cx="890" cy="157" r="12"/>

  <g class="name-label" transform="rotate(-1 622 518)">
    <rect class="name-tag" x="499" y="482" width="247" height="72"/>
    <circle class="name-dot" cx="522" cy="520" r="6"/>
    <circle class="name-dot" cx="722" cy="520" r="6"/>
    <text class="display name-text" x="622" y="532" text-anchor="middle">DALE PRUSKY</text>
  </g>
  <g class="name-label" transform="rotate(-1 909 510)">
    <rect class="name-tag" x="786" y="474" width="246" height="72"/>
    <circle class="name-dot" cx="808" cy="511" r="6"/>
    <circle class="name-dot" cx="1010" cy="511" r="6"/>
    <text class="display name-text" x="909" y="523" text-anchor="middle">TED MARRISH</text>
  </g>
</svg>
</body>
</html>
```